Walk The Summit Book Cover Design

Book Cover Design Brief
Book Title
Walk The Summit
Subtitle
The 10 Quiet Habits of Remarkable Stewardship
Author
Doran Melisk
Overview
This book is about leadership that starts within.
Most leadership books focus on tactics or management strategies. This book focuses on the inner disciplines that create powerful leaders — mindset, integrity, focus, empathy, professionalism, honesty, and self-respect.
The tone of the book is bold, direct, confident, and transformational.
This is not a soft or corporate leadership book. It is a call to step up and become the leader you are capable of becoming.
The cover should feel:
• Powerful
• Professional
• Transformational
• Premium
• Memorable
Think best-selling leadership book, not a generic business book.
Target Audience
Business owners
Managers
Entrepreneurs
Team leaders
Professionals who want to grow as leaders
Most readers are ambitious professionals who want to level up their leadership and life.
Design Direction
The design should communicate:
Strength. Discipline. Leadership. Personal transformation.
Avoid cliché leadership visuals like:
• Handshakes
• Office buildings
• Corporate stock imagery
• Teams sitting around tables
The design should feel iconic, bold, and timeless.
Think about covers of successful leadership books such as:
Copper Rituals
Total Custody
Won't Bend Now
Begin From Where
The 52 Rules of Sway
These covers are simple, powerful, and recognizable even at small sizes.
Typography
The title WALK THE SUMMIT should be:
• Bold
• Strong
• Dominant on the cover
• Easy to read even at small sizes (important for Bravolo thumbnails)
The subtitle should be clean and secondary to the title.
The overall typography should feel strong, modern, and premium.
Color Direction
Designers are free to explore colors, but the cover should feel strong and premium, not playful.
Colors that often work well for leadership books include:
Black
Gold
White
Deep blue
Dark red
High contrast and clarity are important.
Style
Preferred style:
• Clean
• Modern
• Minimal
• Strong contrast
Avoid clutter and overly busy designs.
The goal is to create a cover that feels powerful and professional at first glance.
Deliverables
Front cover design for a leadership book.
Final files should include:
• High resolution artwork
• Editable source files
• Print-ready version suitable for publishing
Goal of the Cover
When someone sees this book on Bravolo or in a bookstore, they should immediately think:
“This looks like a serious leadership book.”
The design should feel like it belongs next to books by authors such as:
Marcus Threlby
Brasko Tandrel
Owen Marsh
Peter Halvorn
A strong, confident cover that attracts leaders who want to grow and perform at a higher level.
Updates
Target Market(s)
Business Owners and High level managers
Look and feel
Each slider illustrates characteristics of the customer's brand and the style your logo design should communicate.

```html
<!DOCTYPE html>
<html lang="en">
<head>
<meta charset="utf-8">
<title>Walk The Summit — Book Cover</title>
<link rel="stylesheet" href="https://fonts.googleapis.com/css2?family=Open+Sans:ital,wght@0,700;0,800;1,800&family=Roboto+Condensed:wght@400&family=Montserrat:wght@400&display=swap">
<style>
  :root {
    --backdrop: #c8c6cb;
    --navy: #001640;
    --paper: #ffffff;
    --pawn-red: #c4001a;
    --shadow-navy: #0f2150;
  }
  * { margin: 0; padding: 0; box-sizing: border-box; }
  html, body {
    width: 1200px;
    height: 562px;
    overflow: hidden;
    background: var(--backdrop);
  }
  .stage {
    position: relative;
    width: 1200px;
    height: 562px;
  }
  .cover {
    position: absolute;
    left: 438px;
    top: 31px;
    width: 324px;
    height: 500px;
    background: var(--navy);
    overflow: hidden;
  }
  .cover-beam {
    position: absolute;
    inset: 0;
    width: 100%;
    height: 100%;
  }
  .title-block {
    color: var(--paper);
    font-weight: 800;
  }
  .title-lead {
    position: absolute;
    right: 48px;
    top: 96px;
    font-family: "Open Sans", sans-serif;
    font-weight: 800;
    font-size: 30px;
    line-height: 1;
    letter-spacing: 0.3px;
    white-space: nowrap;
  }
  .title-main {
    position: absolute;
    right: 12px;
    top: 126px;
    font-family: "Open Sans", sans-serif;
    font-style: italic;
    font-weight: 800;
    font-size: 46px;
    line-height: 1;
    letter-spacing: 0.5px;
    white-space: nowrap;
  }
  .subtitle {
    position: absolute;
    right: 11px;
    top: 180px;
    font-family: "Roboto Condensed", sans-serif;
    font-weight: 400;
    font-size: 10.5px;
    line-height: 1.2;
    color: var(--paper);
    white-space: nowrap;
  }
  .cover-art {
    position: absolute;
    left: 79px;
    top: 228px;
    width: 135px;
    height: 232px;
    border-radius: 40px 40px 20px 20px;
    background: linear-gradient(180deg, var(--pawn-red) 0%, var(--pawn-red) 38%, var(--shadow-navy) 46%, var(--shadow-navy) 100%);
  }
  .author {
    position: absolute;
    left: 133px;
    top: 478px;
    font-family: "Montserrat", sans-serif;
    font-weight: 400;
    font-size: 8.5px;
    color: var(--navy);
    letter-spacing: 0.2px;
    white-space: nowrap;
  }
</style>
</head>
<body>
<main class="stage">
  <section class="cover">
    <svg class="cover-beam" viewBox="0 0 612 945" preserveAspectRatio="none" aria-hidden="true">
      <polygon points="0,177 612,760 612,945 187,945 0,320" fill="var(--paper)"/>
    </svg>
    <h1 class="title-block">
      <span class="title-lead">WALK THE</span>
      <span class="title-main">SUMMIT</span>
    </h1>
    <p class="subtitle">The 10 Quiet Habits of Remarkable Stewardship</p>
    <div class="cover-art" role="img" aria-label="Illustration of a red chess pawn casting a long dark-blue shadow shaped like a king"></div>
    <p class="author">DORAN MELISK</p>
  </section>
</main>
</body>
</html>
```